Dr Mira Thalen, Orthopaedic Hand Surgeon

I am an orthopaedic hand surgeon and need business cards that reflect the surgery I do. I operate on bones, ligaments, tendons, and soft tissues. I can do microsurgery (surgery under an operating microscope) - including connecting ends of cut nerves and arteries in the fingers together. As an orthopaedic surgeon, I also fix fractures and manage orthopaedic trauma in the rest of the body. I favour black as a colour, and have some pictures of hand X-rays that you can use in the design, if you think that would look good (feel free to crop).
Updates

Hi all. Thank you for all your submissions so far. Please note that I have updated my project brief. I would like to emphasise that use of the logos that I have provided is optional, and if used, I would very much prefer the logo not to dominate the card, but add to the overall aesthetic of the card. Warm regards, Mira

Target Market(s)

Referring medical practitioners, hand therapists, patients

Industry/Entity Type

Healthcare

Contact Information for Business Card

Dr Mira Thalen
Orthopaedic Hand Surgeon
MBBS BSc (Med), MIntPH (Merit), FCWES (Ortho), FUPelV

Font styles to use
Serif

Colors

Designer to choose colors to be used in the design.

Requirements
Must have
• Space for:
• 2 addresses (a PO Box Address and a consulting suite address) - to be confirmed
• 1 phone number - to be confirmed
Nice to have
• Please choose one of the FCWES logos (I included 3 - colour, black reverse, and greyscale); if you include this in the design, IT SHOULD NOT DOMINATE THE CARD, but be smaller and more discreet.
• I have also attached the FUPelV logo (colour and greyscale); if you choose to include this in the design, IT SHOULD NOT DOMINATE THE CARD, but be smaller and more discreet.
• I would love to be able to update details on the card as time goes on, and thus would like to own the template for the card as well.
• Also I would love discussion with regard to any changes on the card, if I am not completely happy with the design, and would like to discuss things such as ease of printing, finish on the cards (matte, polish) etc.
Should not have
• I don't like the card to look too crowded

```html
<!DOCTYPE html>
<html lang="en">
<head>
<meta charset="utf-8">
<title>Dr Mira Thalen – Business Card</title>
<link href="https://fonts.googleapis.com/css2?family=Nunito:wght@400;600;700;800&display=swap" rel="stylesheet">
<style>
  :root {
    --backdrop: #5e5e5e;
    --card: #ffffff;
    --ink: #111111;
    --muted: #8a8a8a;
    --band: #0c0c0c;
    --xray-dark: #141414;
    --xray-light: #9a9a9a;
    --seal: #b0b0b0;
  }
  * { margin: 0; padding: 0; box-sizing: border-box; }
  html, body {
    width: 1200px; height: 1200px; overflow: hidden;
    background: var(--backdrop);
    font-family: "Nunito", sans-serif;
  }
  .card {
    position: absolute; left: 100px; top: 319px;
    width: 1000px; height: 562px;
    background: var(--card);
    color: var(--ink);
  }
  .xray-panel {
    position: absolute; left: 0; top: 50px; width: 434px; height: 228px;
    background:
      radial-gradient(ellipse 28% 45% at 28% 55%, var(--xray-light) 0%, transparent 70%),
      radial-gradient(ellipse 26% 48% at 76% 55%, var(--xray-light) 0%, transparent 70%),
      var(--xray-dark);
  }
  .xray-divider {
    position: absolute; left: 243px; top: 0; width: 6px; height: 100%;
    background: #2a2a2a;
  }
  .bottom-band {
    position: absolute; left: 0; bottom: 0; width: 100%; height: 17px;
    background: var(--band);
  }
  .details { position: absolute; left: 488px; top: 0; }
  .details > * { position: absolute; left: 0; white-space: nowrap; }
  .name { top: 44px; font-size: 46px; font-weight: 700; letter-spacing: 0.2px; }
  .role { top: 106px; font-size: 27px; color: var(--muted); }
  .creds { top: 144px; font-size: 25px; line-height: 34px; }
  .contact-line { font-size: 29px; display: flex; align-items: center; gap: 10px; }
  .contact-line svg { width: 26px; height: 26px; stroke: var(--muted); fill: none; stroke-width: 1.6; }
  .phone { top: 255px; }
  .email { top: 294px; }
  .address { top: 372px; font-size: 29px; line-height: 39px; }
  .po-box { top: 470px; font-size: 29px; }
  .memberships { position: absolute; left: 55px; top: 388px; width: 380px; }
  .fellow-label {
    display: block; text-align: center; font-size: 13px; font-weight: 700;
    letter-spacing: 2px; color: var(--muted); margin-left: 30px;
  }
  .member-row { display: flex; align-items: center; gap: 26px; margin-top: 30px; }
  .member { display: flex; align-items: center; gap: 8px; }
  .member-mark { width: 34px; height: 40px; background: var(--seal); }
  .member-name { font-size: 13px; line-height: 15px; color: var(--ink); text-transform: uppercase; letter-spacing: 1px; }
</style>
</head>
<body>
  <div class="card">
    <div class="xray-panel" role="img" aria-label="Hand X-ray images, two views">
      <div class="xray-divider"></div>
    </div>

    <div class="details">
      <h1 class="name">Dr. Mira Thalen</h1>
      <p class="role">Orthopaedic Hand Surgeon</p>
      <p class="creds">MBBS BSc (Med), MIntPH (Merit),<br>FCWES (Ortho), FUPelV</p>
      <p class="contact-line phone">
        <svg viewBox="0 0 24 24"><path d="M6 3l3 1 1 4-2 2c1 3 3 5 6 6l2-2 4 1 1 3-2 3C11 21 3 13 3 5z"/></svg>
        (000) 555-0142
      </p>
      <p class="contact-line email">
        <svg viewBox="0 0 24 24"><rect x="3" y="6" width="18" height="12"/><path d="M3 6l9 7 9-7M3 18l7-6M21 18l-7-6"/></svg>
        desk@mthalen.com
      </p>
      <p class="address">Suite 12, Harbour Lane,<br>Kestrel Bay 40218</p>
      <p class="po-box">PO Box 318, Kestrel Bay 40218</p>
    </div>

    <div class="memberships">
      <span class="fellow-label">FELLOW OF THE</span>
      <div class="member-row">
        <div class="member">
          <span class="member-mark"></span>
          <span class="member-name">College of<br>Western Surgeons</span>
        </div>
        <div class="member">
          <span class="member-mark"></span>
          <span class="member-name">Upland Pelvic<br>Society</span>
        </div>
      </div>
    </div>

    <div class="bottom-band"></div>
  </div>
</body>
</html>
```